Tovex - Business Card Design

Design a modern masculine business card for our business

Target Market(s)

Private Market

Industry/Entity Type

Construction

Contact Information for Business Card

Company Name - Name of Person - Address - email address - contact number

Font styles to use
Serif
Sans Serif

Colors
0094D4
00A9DD
6FCCEA
C7EBF8
E9F6FB
00AB8E
00BBA5
67D7C9
C6EFE9
E9F9F6
F0912C
F2A743
F7CA91
FBE8D2
FDF5EE

Requirements
Must have
• Use company logo provided
Nice to have
• Company Logo

```html
<!DOCTYPE html>
<html lang="en">
<head>
<meta charset="utf-8">
<title>Tovex Business Card</title>
<link rel="stylesheet" href="https://fonts.googleapis.com/css2?family=Orbitron:wght@700&family=Montserrat:wght@500&display=swap">
<style>
  :root {
    --stage: #262626;
    --ink: #111111;
    --card-dark: #171717;
    --paper: #ffffff;
    --accent: #f07232;
    --steel: #9a9a9a;
    --band-dark: #000000;
  }
  * { margin: 0; padding: 0; box-sizing: border-box; }
  html, body { width: 900px; height: 1200px; overflow: hidden; background: var(--stage); }
  .canvas { position: relative; width: 900px; height: 1200px; }

  .card { position: absolute; left: 118px; width: 664px; height: 378px; overflow: hidden; }
  .card--front { top: 201px; background: var(--card-dark); }
  .card--back { top: 618px; background: var(--paper); }

  .wordmark {
    display: flex; align-items: center; gap: 14px;
    font-family: "Orbitron", sans-serif; font-weight: 700; letter-spacing: 4px;
  }
  .wordmark__square { display: block; background: var(--accent); }
  .card--front .wordmark {
    position: absolute; inset: 0; justify-content: center;
    font-size: 72px; color: var(--steel);
  }
  .card--front .wordmark__square { width: 22px; height: 22px; }
  .card--back .wordmark {
    position: absolute; left: 66px; top: 158px; font-size: 48px; line-height: 60px; color: var(--ink);
  }
  .card--back .wordmark__square { width: 16px; height: 16px; }

  .divider { position: absolute; left: 332px; top: 97px; width: 1px; height: 185px; background: var(--ink); }

  .details { position: absolute; left: 349px; top: 0; width: 300px; height: 378px; font-family: "Montserrat", sans-serif; font-weight: 500; color: var(--ink); }
  .details > * { position: absolute; left: 0; white-space: nowrap; }
  .details__name { top: 92px; font-family: "Orbitron", sans-serif; font-weight: 700; font-size: 25px; line-height: 28px; color: var(--accent); letter-spacing: 1px; }
  .details__role { top: 122px; font-size: 15px; line-height: 20px; letter-spacing: 1px; }
  .details__rule { width: 78px; height: 2px; background: var(--accent); }
  .details__rule--first { top: 147px; }
  .details__rule--second { top: 204px; }
  .details__line { font-size: 15px; line-height: 20px; letter-spacing: 1px; }
  .details__line--street { top: 155px; }
  .details__line--city { top: 179px; }
  .details__contact { display: flex; align-items: center; gap: 6px; font-size: 15px; line-height: 20px; letter-spacing: 1px; }
  .details__contact--phone { top: 213px; letter-spacing: 3px; }
  .details__contact--email { top: 239px; }
  .details__contact--web { top: 265px; }
  .icon { width: 13px; height: 13px; fill: var(--accent); flex: none; }

  .footer-band {
    position: absolute; left: 0; bottom: 0; width: 664px; height: 20px;
    background: linear-gradient(90deg, var(--accent) 0%, var(--accent) 34%, var(--band-dark) 46%, var(--band-dark) 100%);
  }
</style>
</head>
<body>
<main class="canvas">
  <section class="card card--front" aria-label="Card front">
    <div class="wordmark"><span class="wordmark__square"></span>TOVEX</div>
  </section>

  <section class="card card--back" aria-label="Card back">
    <div class="wordmark"><span class="wordmark__square"></span>TOVEX</div>
    <div class="divider"></div>
    <div class="details">
      <p class="details__name">DALE BRENNAN</p>
      <p class="details__role">President</p>
      <div class="details__rule details__rule--first"></div>
      <p class="details__line details__line--street">2716 Granite Way</p>
      <p class="details__line details__line--city">Kelso, Idaho 83701</p>
      <div class="details__rule details__rule--second"></div>
      <p class="details__contact details__contact--phone">
        <svg class="icon" viewBox="0 0 24 24"><path d="M6.6 10.8a15 15 0 0 0 6.6 6.6l2.2-2.2a1 1 0 0 1 1-.25 11.4 11.4 0 0 0 3.6.57 1 1 0 0 1 1 1V20a1 1 0 0 1-1 1A17 17 0 0 1 3 4a1 1 0 0 1 1-1h3.5a1 1 0 0 1 1 1c0 1.25.2 2.45.57 3.6a1 1 0 0 1-.25 1z"/></svg>555-704-218
      </p>
      <p class="details__contact details__contact--email">
        <svg class="icon" viewBox="0 0 24 24"><path d="M2 5h20v14H2z M2 5l10 8 10-8" stroke="#fff" stroke-width="1.5"/></svg>dale@tovexbuild.net
      </p>
      <p class="details__contact details__contact--web">
        <svg class="icon" viewBox="0 0 24 24"><circle cx="12" cy="12" r="10"/><path d="M2 12h20M12 2c3 3 3 17 0 20M12 2c-3 3-3 17 0 20M4 7h16M4 17h16" stroke="#fff" stroke-width="1.2" fill="none"/></svg>www.tovexbuild.net
      </p>
    </div>
    <div class="footer-band" role="img" aria-label="Decorative orange and black footer band"></div>
  </section>
</main>
</body>
</html>
```